Mental Health Services for Employees - we need a website for our new business

We need a simple web design to showcase our various services. Our programs help organizations to ensure the heath and wellness of their workers. Our company is called "Brightway Workplace Partners Inc." or "Brightway" We'd like to see designs that use the colour palette from our logo. Our customers our fairly conservative, and our design should communicate due diligence around providing a safe and healthy environment for workers. Attached our the logo files. Also sample photographs from our purchased images - others available. Original design for website is found here: https://lanternow7.examplesite.com/mypage-1 A key page not listed in our original design is a section that lists "Five Reasons to Work With Us". We will need to be able to modify and change the copy/menu options as the business grows.

Target Market(s)

businesses who want to provide health and wellness services for their employees

Coding

Coded - Design and coding required

Number of Pages Required

2 page

Font styles to use
Sans Serif

Requirements
Must have
• colours that work with our attached logo

```html
<!DOCTYPE html>
<html lang="en">
<head>
<meta charset="utf-8">
<title>Brightway Workplace Partners Inc.</title>
<link rel="stylesheet" href="https://fonts.googleapis.com/css2?family=Montserrat:wght@400;500;600;700;900&display=swap">
<style>
:root{
  --orange:#f5ae3c;
  --teal:#0fb09f;
  --teal-soft:#d3f0ec;
  --ink:#2b2b2b;
  --text:#333;
  --white:#fff;
  --card:#f5f5f5;
  --field:#f3f3f3;
  --black:#000;
}
*{box-sizing:border-box;margin:0;padding:0}
html,body{width:1200px;height:3522px;overflow:hidden}
body{font-family:"Montserrat",Arial,sans-serif;color:var(--text);background:var(--white);position:relative}
.abs{position:absolute}
/* header */
.site-header{position:absolute;top:0;left:0;width:1200px;height:83px;background:var(--white)}
.brand{position:absolute;left:115px;top:24px;display:flex;align-items:center;gap:10px;font-weight:700;font-size:28px;color:var(--ink);letter-spacing:.5px}
.brand-mark{width:14px;height:14px;background:var(--teal)}
.main-nav{position:absolute;top:0;left:647px;display:flex;font-size:12.5px;font-weight:500;color:var(--ink)}
.main-nav a{display:block;height:72px;line-height:74px;padding:0 9px;color:inherit;text-decoration:none}
.main-nav a.active{background:var(--teal-soft);padding:0 10px}
/* hero */
.hero{position:absolute;top:83px;left:0;width:1200px;height:591px;background:linear-gradient(100deg,#7f7468 0%,#5e554d 35%,#8d8378 60%,#b9b3ab 100%)}
.hero::after{content:"";position:absolute;inset:0;background:rgba(0,0,0,.22)}
.hero-content{position:absolute;z-index:1;left:0;width:1200px;top:265px;text-align:center;color:var(--white)}
.hero h1{font-weight:900;font-size:41px;line-height:49px;letter-spacing:.2px}
.hero p{font-size:15px;line-height:19px;margin-top:22px;font-weight:500}
.btn-teal{display:inline-block;background:var(--teal);color:var(--white);font-size:11px;font-weight:600;height:32px;line-height:32px;width:98px;margin-top:30px}
.slider-arrow{position:absolute;z-index:1;top:303px;width:58px;height:58px;border-radius:50%;background:rgba(40,40,40,.75)}
.slider-arrow svg{position:absolute;left:21px;top:20px}
/* section titles */
.section-title{position:absolute;left:0;width:1200px;text-align:center;font-weight:500;font-size:33px;color:var(--ink)}
/* services */
.services-intro{position:absolute;top:842px;left:0;width:1200px;text-align:center;font-size:11.5px;line-height:20px}
.service-card{position:absolute;top:920px;width:250px;height:291px;background:var(--card)}
.service-photo{height:191px}
.service-card .label{height:100px;display:flex;flex-direction:column;justify-content:center;text-align:center;font-size:15px;line-height:25px;color:var(--ink)}
.service-card .label small{font-size:10.5px;line-height:21px}
/* about */
.about{position:absolute;top:1281px;left:0;width:1200px;height:618px;background:var(--orange)}
.about h2{position:absolute;left:113px;top:96px;font-size:32px;font-weight:500;color:var(--white)}
.about-copy{position:absolute;left:113px;top:152px;width:345px;font-size:12.5px;line-height:16.6px;color:var(--white);font-weight:500}
.about-copy p{margin-bottom:16px;text-indent:5px}
.about-copy p+p{text-indent:40px}
.btn-white{position:absolute;left:113px;top:512px;width:92px;height:32px;line-height:32px;text-align:center;background:var(--white);color:var(--ink);font-size:11px;font-weight:500}
.about-photo{position:absolute;left:625px;top:75px;width:467px;height:466px;background:linear-gradient(160deg,#c9c2b4 0%,#d88a4a 55%,#e55f25 100%)}
/* portfolio */
.portfolio-tile{position:absolute;top:2029px;height:270px}
/* reasons */
.reasons{position:absolute;top:2302px;left:0;width:1200px;height:413px;background:var(--teal);color:var(--white)}
.reasons-photo{position:absolute;left:113px;top:48px;width:356px;height:317px;background:linear-gradient(180deg,#d8d5cf 0%,#b7ad9f 45%,#6f5a43 75%,#4b4037 100%)}
.reasons h2{position:absolute;left:514px;top:100px;font-size:33px;font-weight:500}
.reasons ol{position:absolute;left:517px;top:170px;list-style:none;font-size:15px;line-height:30px;font-weight:500}
/* contact */
.col-title{position:absolute;font-size:22px;font-weight:500;color:var(--ink)}
.copy{position:absolute;font-size:13.5px;line-height:20.5px;color:var(--ink)}
.field{position:absolute;left:239px;width:351px;background:var(--field);font-size:12px;color:#999;padding:5px 10px}
.btn-submit{position:absolute;left:467px;top:3199px;width:123px;height:31px;line-height:31px;text-align:center;background:var(--teal);color:var(--white);font-size:13px;font-weight:600}
/* footer */
.site-footer{position:absolute;top:3357px;left:0;width:1200px;height:165px;background:var(--black);color:#888}
.social{position:absolute;top:53px;left:0;width:1200px;display:flex;justify-content:center;gap:24px}
.social span{width:12px;height:12px;border-radius:50%;background:#777}
.copyright{position:absolute;top:101px;left:0;width:1200px;text-align:center;font-size:11px}
</style>
</head>
<body>

<header class="site-header">
  <div class="brand"><span class="brand-mark"></span>Brightway</div>
  <nav class="main-nav">
    <a class="active">Home</a><a>SERVICES</a><a>ABOUT</a><a>SAP</a><a>REFFERALS</a><a>CONTACT US</a><a>PORTAL</a>
  </nav>
</header>

<section class="hero" role="img" aria-label="Photo of a counsellor talking with a client">
  <div class="slider-arrow" style="left:15px"><svg width="16" height="18" viewBox="0 0 16 18"><path d="M11 2 L4 9 L11 16" fill="none" stroke="#fff" stroke-width="2"/></svg></div>
  <div class="slider-arrow" style="left:1127px"><svg width="16" height="18" viewBox="0 0 16 18"><path d="M5 2 L12 9 L5 16" fill="none" stroke="#fff" stroke-width="2"/></svg></div>
  <div class="hero-content">
    <h1>HELPING ORGANIZATIONS<br>MAINTAIN A SAFE WORKPLACE</h1>
    <p>Lorem ipsum dolor sit amet, consectetur adipisicing elit, sed do eiusmod<br>tempor incididunt ut labore et dolore magna aliqua.</p>
    <span class="btn-teal">READ MORE</span>
  </div>
</section>

<h2 class="section-title" style="top:788px">OUR SERVICES</h2>
<p class="services-intro">Lorem ipsum dolor sit amet, consectetur adipisicing elit, sed do eiusmod tempor<br>incididunt ut labore et dolore magna aliqua. .</p>

<article class="service-card" style="left:208px">
  <div class="service-photo" role="img" aria-label="Photo of a support group reaching out" style="background:linear-gradient(135deg,#e6e2dc,#6d8db3 55%,#c9b9a8)"></div>
  <div class="label">Accomodation<br>Screening</div>
</article>
<article class="service-card" style="left:475px">
  <div class="service-photo" role="img" aria-label="Photo of a person in a group session" style="background:linear-gradient(135deg,#8c8a7e,#c9c37a 40%,#4f5a6e)"></div>
  <div class="label">SAP Assessments<small>DOT and NON DOT<br>Substance Abuse Professional</small></div>
</article>
<article class="service-card" style="left:742px">
  <div class="service-photo" role="img" aria-label="Photo of a seated group discussion" style="background:linear-gradient(135deg,#b88a5e,#d9c6a8 45%,#5f6f6a)"></div>
  <div class="label">Specialized Addiction Case<br>Management</div>
</article>

<section class="about">
  <h2>ABOUT US</h2>
  <div class="about-copy">
    <p>Brightway Workplace Partners Inc. ("Brightway") provides outstanding business-to-business services that support and promote health, wellness, and safety in the workplace. Brightway's flagship programs are the Substance Abuse Professional (SAP) and Specialized Addiction Case Management services.</p>
    <p>Brightway is ready to provide organizations with access to a suite of best-practice solutions and options for your employees. These services empower organizations to effectively deal with substance use, to understand and fulfill various legislative and/or policy requirements, and to help keep their workers safe and healthy.</p>
    <p>Whenever organizations have a need to address substance use in the workplace please consider us a resource to help with program development based on the locations and specific needs of your employees.</p>
  </div>
  <span class="btn-white">Read More</span>
  <div class="about-photo" role="img" aria-label="Photo of a worker in a yellow hard hat and orange jacket"></div>
</section>

<h2 class="section-title" style="top:1962px">PORTFOLIO</h2>
<div class="portfolio-tile" role="img" aria-label="Photo of workers silhouetted by an oil pump" style="left:0;width:290px;background:linear-gradient(180deg,#2d5fb0,#6f95d4 55%,#10141c)"></div>
<div class="portfolio-tile" role="img" aria-label="Photo of a worker cutting a log" style="left:294px;width:303px;background:linear-gradient(135deg,#4c5a3e,#8a8f82 50%,#c45a3c)"></div>
<div class="portfolio-tile" role="img" aria-label="Photo of a worker in a white hard hat" style="left:600px;width:304px;background:linear-gradient(135deg,#6a5a3a,#d8b07a 50%,#c77a3b)"></div>
<div class="portfolio-tile" role="img" aria-label="Photo of a yellow hard hat and safety vest" style="left:906px;width:294px;background:linear-gradient(135deg,#e8d11a,#d6e24a 50%,#b8743a)"></div>

<section class="reasons">
  <div class="reasons-photo" role="img" aria-label="Photo of a mining haul truck"></div>
  <h2>FIVE REASONS TO WORK WITH US</h2>
  <ol>
    <li>1. Lorem ipsum dolor sit amet, consectetur adipisicing elit.</li>
    <li>2. Sed do eiusmod tempor incididunt ut labore et dolore.</li>
    <li>3. Magna aliqua. Ut enim ad minim veniam, quis nostrud.</li>
    <li>4. Exercitation ullamco laboris nisi ut aliquip ex ea commodo.</li>
    <li>5. Consequat. Duis aute irure dolor in reprehenderit in voluptate</li>
  </ol>
</section>

<h2 class="section-title" style="top:2796px">CONTACT</h2>

<h3 class="col-title" style="left:238px;top:2871px">Send us a message</h3>
<p class="copy" style="left:239px;top:2921px">For any inquiries, questions or referrals,<br>please call: 888-555-0142 or fill out the follow-</p>
<div class="field" style="top:2992px;height:23px">Name</div>
<div class="field" style="top:3023px;height:23px">Email</div>
<div class="field" style="top:3055px;height:23px">Subject</div>
<div class="field" style="top:3088px;height:104px;padding-top:10px">Message</div>
<span class="btn-submit">Submit</span>

<h3 class="col-title" style="left:698px;top:2871px">Head Office</h3>
<p class="copy" style="left:698px;top:2921px">118 Harbourview Avenue, Suite 300<br>Toronto Ontario, M4C 2T7</p>
<p class="copy" style="left:698px;top:2984px">coordinators@brightway-wp.com<br>Tel:&nbsp; 888-555-0142<br>Fax: 416-555-0198</p>
<h3 class="col-title" style="left:698px;top:3075px">Employment</h3>
<p class="copy" style="left:698px;top:3119px">To become a SAP affiliate with Bright-<br>way, please read the SAP informa-<br>tion page for minimum require-<br>ments before sending a cover letter<br>coordinators@brightway-wp.com</p>
<p class="col-title" style="left:698px;top:3266px">Get a SAP: 888-555-0142</p>

<footer class="site-footer">
  <div class="social" aria-label="Social links"><span></span><span></span><span></span><span></span></div>
  <p class="copyright">© 2019 Brightway Workplace Partners Inc.</p>
</footer>

</body>
</html>
```